Freelancer Information Security professional needs a business card

I need a simple, young, elegant business card. I'm a freelancer in the InfoSec area and want to be able to give my card to potential customers and new people I meet.

I'd like to have a clean, professional look but at same time not boring or corporate.

The only requirement is to have my "introduction" phrase which is:
"Half hacker, half mercenary."

I have added a card I have as a example, which I think it gives a good example of style I want.

Target Market(s)

Technology / Computers / Engineering

Industry/Entity Type

Information Technology

Contact Information for Business Card

Contact fields I want included:

(351) 93 708 16 52
tomas@vorelin.im
https://vorelin.im

Font styles to use
Sans Serif

Requirements
Nice to have
• Card doesn't need to have a doubled side, but it looks good / fits the design then please do include.
Should not have
• Outdated graphics or images; too much patterns/colors.

```html
<!DOCTYPE html>
<html lang="en">
<head>
<meta charset="utf-8">
<title>Nadia Ferrol — Business Card</title>
<link href="https://fonts.googleapis.com/css2?family=Jost:wght@400;500;600&display=swap" rel="stylesheet">
<style>
  :root {
    --page: #e9e8e5;
    --card: #fbfbfb;
    --ink: #111111;
    --muted: #2b2b2b;
    --accent: #2f4fa8;
    --rule: #3a3a3a;
  }
  html, body {
    margin: 0;
    width: 1200px;
    height: 902px;
    overflow: hidden;
    background: var(--page);
    font-family: "Jost", "Century Gothic", sans-serif;
  }
  .card {
    position: absolute;
    left: 100px;
    top: 166px;
    width: 1000px;
    height: 570px;
    background: var(--card);
    box-shadow: 0 10px 30px rgba(0,0,0,0.15);
  }
  .tagline {
    position: absolute;
    left: 92px;
    top: 92px;
    margin: 0;
    font-size: 66px;
    font-weight: 600;
    color: var(--ink);
    letter-spacing: -0.5px;
    white-space: nowrap;
  }
  .divider {
    position: absolute;
    left: 560px;
    top: 230px;
    width: 1.5px;
    height: 232px;
    background: var(--rule);
  }
  .identity {
    position: absolute;
    right: 470px;
    top: 348px;
    text-align: left;
  }
  .identity-name {
    margin: 0;
    font-size: 54px;
    font-weight: 600;
    color: var(--accent);
    line-height: 1;
    letter-spacing: -0.5px;
  }
  .identity-role {
    margin: 6px 0 0 22px;
    font-size: 24px;
    font-weight: 500;
    color: var(--muted);
  }
  .contacts {
    position: absolute;
    left: 600px;
    top: 250px;
    margin: 0;
    padding: 0;
    list-style: none;
  }
  .contact-item {
    display: flex;
    align-items: center;
    gap: 14px;
    height: 42px;
    font-size: 25px;
    color: var(--muted);
  }
  .contact-icon {
    width: 26px;
    height: 26px;
    flex: none;
  }
</style>
</head>
<body>
  <div class="card">
    <h1 class="tagline">"Half hacker, half mercenary."</h1>

    <div class="identity">
      <p class="identity-name">Nadia Ferrol</p>
      <p class="identity-role">Chief Creative Officer</p>
    </div>

    <div class="divider"></div>

    <ul class="contacts">
      <li class="contact-item">
        <svg class="contact-icon" viewBox="0 0 26 26" aria-hidden="true">
          <rect width="26" height="26" rx="6" fill="var(--accent)"/>
          <path d="M7 10c0-2 2-3 6-3s6 1 6 3l-2 1-1-2h-6l-1 2z" fill="#fff"/>
          <rect x="8" y="12" width="10" height="7" rx="2" fill="#fff"/>
          <circle cx="13" cy="15.5" r="1.8" fill="var(--accent)"/>
        </svg>
        <span>(351) 93 708 16 52</span>
      </li>
      <li class="contact-item">
        <svg class="contact-icon" viewBox="0 0 26 26" aria-hidden="true">
          <rect width="26" height="26" rx="6" fill="var(--accent)"/>
          <rect x="6" y="8" width="14" height="10" rx="1" fill="#fff"/>
          <path d="M6.5 8.5l6.5 5 6.5-5" fill="none" stroke="var(--accent)" stroke-width="1.4"/>
        </svg>
        <span>tomas@vorelin.im</span>
      </li>
      <li class="contact-item">
        <svg class="contact-icon" viewBox="0 0 26 26" aria-hidden="true">
          <rect width="26" height="26" rx="6" fill="var(--accent)"/>
          <g fill="none" stroke="#fff" stroke-width="1.4">
            <circle cx="13" cy="13" r="6.5"/>
            <ellipse cx="13" cy="13" rx="3" ry="6.5"/>
            <path d="M6.5 13h13M7.5 9.8h11M7.5 16.2h11"/>
          </g>
        </svg>
        <span>https://vorelin.im</span>
      </li>
    </ul>
  </div>
</body>
</html>
```